Twirly Puff Cotton Candy

Looking for a logo design and business cards to help a 13 year old entrepreneur promote her cotton candy business.
Contact Information for Business Card
Name, Phone & Email
Colors
E54698
E96AAD
F1A4CE
F9D9EA
FCEFF6
A7469A
B969AE
D3A5CF
EDDBEB
F8F0F9
6B429C
8869AF
B7A5CE
E3DAEB
F3F0F8
Requirements
Must have
- A fun feel that is appropriate for a teenage girl selling cotton candy

```html
<!DOCTYPE html>
<html lang="en">
<head>
<meta charset="UTF-8">
<title>Twirly Puff Cotton Candy – Business Cards</title>
<link rel="stylesheet" href="https://fonts.googleapis.com/css2?family=Poppins:wght@600&family=Roboto:wght@400&display=swap">
<style>
  :root {
    --backdrop: #2a2524;
    --card: #1b1b1b;
    --pink: #e54698;
    --purple: #6b429c;
    --purple-text: #8869af;
    --divider: #8a8a8a;
  }
  * { box-sizing: border-box; margin: 0; padding: 0; }
  html, body {
    width: 1200px;
    height: 842px;
    overflow: hidden;
    background: var(--backdrop);
  }
  .canvas {
    position: relative;
    width: 1200px;
    height: 842px;
  }
  .card {
    position: absolute;
    top: 266px;
    width: 540px;
    height: 310px;
    background: var(--card);
    box-shadow: 0 14px 30px rgba(0,0,0,0.5);
    overflow: hidden;
  }
  .card--back { left: 40px; }
  .card--front { left: 620px; }

  /* Back: bands along top and bottom */
  .band {
    position: absolute;
    left: 0;
    width: 100%;
    height: 16px;
    background: var(--pink);
  }
  .band--top { top: 0; border-bottom: 4px solid var(--purple); height: 20px; }
  .band--bottom { bottom: 0; border-top: 4px solid var(--purple); height: 20px; }

  .contact {
    position: absolute;
    left: 0;
    top: 96px;
    width: 100%;
    text-align: center;
  }
  .contact__name {
    font-family: "Poppins", sans-serif;
    font-weight: 600;
    font-size: 26px;
    line-height: 1;
    color: var(--pink);
    letter-spacing: 0.5px;
  }
  .contact__title {
    font-family: "Roboto", sans-serif;
    font-size: 18px;
    line-height: 1.1;
    color: var(--purple-text);
    margin-top: 2px;
  }
  .contact__divider {
    width: 150px;
    height: 1px;
    margin: 12px auto 14px;
    background: var(--divider);
  }
  .contact__line {
    font-family: "Roboto", sans-serif;
    font-size: 19px;
    line-height: 1.3;
    color: var(--purple-text);
  }

  /* Front: side tabs */
  .tab {
    position: absolute;
    width: 40px;
    height: 62px;
    background: var(--pink);
  }
  .tab--left { left: 0; top: 86px; border-right: 4px solid var(--purple); width: 44px; }
  .tab--right { right: 0; top: 86px; border-left: 4px solid var(--purple); width: 44px; }

  .brand {
    position: absolute;
    left: 0;
    top: 0;
    width: 100%;
    height: 100%;
    display: flex;
    flex-direction: column;
    align-items: center;
    justify-content: center;
    gap: 14px;
  }
  .brand__dot {
    width: 64px;
    height: 64px;
    border-radius: 50%;
    background: var(--pink);
  }
  .brand__name {
    font-family: "Poppins", sans-serif;
    font-weight: 600;
    font-size: 30px;
    line-height: 1.05;
    color: var(--pink);
    text-align: center;
  }
</style>
</head>
<body>
<main class="canvas">
  <section class="card card--back" aria-label="Business card, contact side">
    <div class="band band--top"></div>
    <div class="contact">
      <p class="contact__name">Jordan Ellis</p>
      <p class="contact__title">Managing Director</p>
      <div class="contact__divider"></div>
      <p class="contact__line">044-987 654 321</p>
      <p class="contact__line">hello@twirlypuff.com</p>
    </div>
    <div class="band band--bottom"></div>
  </section>

  <section class="card card--front" aria-label="Business card, brand side">
    <div class="tab tab--left"></div>
    <div class="tab tab--right"></div>
    <div class="brand">
      <div class="brand__dot"></div>
      <p class="brand__name">Twirly Puff<br>Cotton Candy</p>
    </div>
  </section>
</main>
</body>
</html>
```